依頼詳細
今回の依頼では、トップページのデザインを考えていただきたいと思っています。
重要視しているのは、とにかく弊社パティスリーの世界観を伝えていただけるデザインです。
ヤギのクラリスや、現サイトの店舗写真などを見ていただくと分かるように、少しコンテンポラリーアートのような要素もあり、かわいらしさもあり、という感じです。
ヤギのクラリスは、既にかなりコアなファンもいるキャラクターで、Tシャツ、マグカップなどの雑貨も販売しています。これらのデザインも可能であれば、参考にしていただいて、デザインしていただければと思っています。現自社サイトの他に、SOLBE_RUNELLEのInstagramなども見ていただければ参考になると思います。
トップページ作成に必要なデータなどありましたら、ご連絡いただければと思います。

今回のコンペでお任せすることになれば、今後につきましても、継続的にその他のページや、メンテナンスについてもお任せしていきたいとおもいますので、ご相談をさせていただき、進めていきたいと思っております。
サイトURL
http://mokuren-kashi.jp/
ページ数
1ページ
希望イメージ
シンプル 複雑
単色 カラフル
暗い 明るい
日常 高級
遊び心 厳粛
未来的 伝統的
女性的 男性的
一度、現行のサイトは忘れていただいて、皆様の新しいアイデアでデザインを考えていただければと思います。
締切を延長いたします。
トップページのデザインは、現行のサイトは無視して、新しいアイデアでデザインをしていただけたらと思います。よろしくお願いいたします。
皆様、ごの度はソルベリュンヌのWEBデザインへのご提案ありがとうございます。素敵な作品ばかりで、選考に難航しており、お時間をいただいております。
本日中には決定したいと思っておりますが、当選にかかわらず、今後、直接依頼などでソルベリュンヌのサイト運営にお力添えいただければと思っておりますので、ご協力いただける場合、またその旨お知らせいただければさいわいです。
よろしくお願いいたします。

トップのデザインを考えていただきたいという意図をとても良く汲んでいただき、かわいらしいデザインのイラストを作っていただきました。修正依頼にも快く応じていただき、今後ともぜひお付き合いさせていただきたいQUILLBOX様でした。

皆様、ご連絡が大変遅くなり申し訳ございません。どの提案も素敵で、甲乙つけがたく、お時間いただいてしまいました。今回お願いしたソルベリュンヌの他、ヤギミルクパンのFERNLOAF、材料のヤギミルクをつくるそよかぜ農園の3つを融合したサイトを作成してまいります。今回、当選とならなかった皆様にもぜひ直接依頼などで今後ぜひお手伝いいただき、サイトを充実させていきたいと思っております。よろしくお願い申し上げます。

```html
<!DOCTYPE html>
<html lang="ja">
<head>
<meta charset="utf-8">
<title>PÂTISSERIE SOLBE RUNELLE</title>
<link rel="stylesheet" href="https://fonts.googleapis.com/css2?family=Noto+Sans+JP:wght@400;500;700&family=Noto+Serif+JP:wght@500;700&family=Cormorant+Garamond:wght@500;600&display=swap">
<style>
:root{
  --red:#c21f1a;
  --red-dark:#a41612;
  --black:#0e0d0c;
  --ink:#2b2623;
  --muted:#7a716b;
  --line:#ddd6cf;
  --white:#ffffff;
  --paper:#fbf8f4;
  --bread-light:#f0cf95;
  --bread:#d69b52;
  --bread-dark:#8b5a2b;
}
*{box-sizing:border-box;margin:0;padding:0}
html,body{width:1200px;height:5388px;overflow:hidden}
body{font-family:"Noto Sans JP",sans-serif;color:var(--ink);background:var(--white);position:relative;font-size:13px;line-height:1.9}
.abs{position:absolute}
.photo{position:absolute;border-radius:2px}
.eyebrow{font-family:"Cormorant Garamond",serif;color:var(--red);font-size:12px;letter-spacing:.2em;text-align:center;font-weight:600}
.section-title{font-family:"Noto Serif JP",serif;font-size:24px;font-weight:700;text-align:center;letter-spacing:.08em}
.btn{position:absolute;display:flex;align-items:center;justify-content:center;gap:14px;font-size:13px;letter-spacing:.08em;color:var(--white);text-decoration:none}
.btn-black{background:var(--black)}
.btn-red{background:var(--red)}
.btn::after{content:"";width:18px;height:1px;background:currentColor}

/* header / hero */
.hero{position:absolute;left:0;top:0;width:1200px;height:600px;overflow:hidden}
.hero-photo{left:0;top:0;width:1200px;height:600px;background:radial-gradient(ellipse at 62% 45%,var(--bread-light) 0%,var(--bread) 35%,var(--bread-dark) 70%,#3d2716 100%)}
.hero-shade{position:absolute;inset:0;background:linear-gradient(90deg,rgba(30,18,10,.45) 0%,rgba(30,18,10,.1) 60%,rgba(30,18,10,0) 100%)}
.global-nav{position:absolute;top:0;left:0;width:1200px;height:64px;display:flex;justify-content:center;align-items:center}
.global-nav a{color:var(--white);font-size:11px;letter-spacing:.2em;text-decoration:none;font-family:"Cormorant Garamond",serif;font-weight:600}
.nav-left,.nav-right{display:flex;gap:60px;width:300px}
.nav-left{justify-content:flex-end;padding-right:40px}
.nav-right{padding-left:40px}
.brand-block{width:180px;height:88px;background:var(--red);display:flex;flex-direction:column;align-items:center;justify-content:center;align-self:flex-start;color:var(--white);font-family:"Noto Serif JP",serif;font-weight:700;line-height:1.2;text-align:center}
.brand-block .l1{font-size:13px;letter-spacing:.12em}
.brand-block .l2{font-size:15px;letter-spacing:.08em}
.social{position:absolute;top:24px;right:40px;display:flex;gap:12px}
.social span{width:14px;height:14px;border-radius:50%;background:var(--white);opacity:.9}
.hero-title{left:380px;top:128px;color:var(--white);font-family:"Noto Serif JP",serif;font-weight:700;font-size:46px;line-height:1.08;letter-spacing:.06em}
.hero-lead{left:380px;top:238px;color:var(--white);font-size:12px;line-height:1.8;font-weight:500}
.banner{position:absolute;top:290px;height:96px;width:232px;border:3px solid var(--white);overflow:hidden}
.banner-bun{left:250px;background:linear-gradient(90deg,#b77336,#e7b574 55%,#fbe9cf)}
.banner-bun .txt{position:absolute;right:12px;top:16px;font-family:"Noto Serif JP",serif;font-weight:700;color:var(--ink);font-size:17px;line-height:1.2;text-align:right}
.banner-bun .txt small{display:block;font-size:9px;color:var(--red);letter-spacing:.1em}
.banner-rank{left:494px;background:linear-gradient(90deg,#fff6e6,#fff)}
.banner-rank .seal{position:absolute;left:12px;top:18px;width:54px;height:54px;border-radius:50%;background:#e2b23c}
.banner-rank .txt{position:absolute;left:78px;top:12px;font-size:10px;font-weight:700;color:var(--ink);line-height:1.5}
.banner-rank .txt b{display:block;color:var(--red);font-size:20px;font-family:"Noto Serif JP",serif}

/* about */
.about-caption{left:60px;top:690px;background:var(--white);border:1px solid var(--red);color:var(--red);font-size:12px;padding:2px 14px;transform:rotate(-3deg);font-weight:500}
.about-photo{left:60px;top:730px;width:540px;height:320px;background:linear-gradient(135deg,#d9d2c8 0%,#b3231c 40%,#e8e4dd 75%,#c8c0b5 100%)}
.about-text{left:720px;top:760px;width:340px}
.about-text .eyebrow,.about-text .section-title{text-align:left}
.about-text .section-title{font-size:22px;margin:4px 0 20px}
.about-text p{font-size:12px;line-height:2.1;margin-bottom:14px;color:var(--ink)}
.about-btn{position:relative;width:140px;height:40px;margin-top:10px}

/* feature (black) */
.feature{position:absolute;left:0;top:1200px;width:1200px;height:1420px;background:var(--black);color:var(--white)}
.tag-red{display:inline-block;background:var(--red);color:var(--white);font-size:10px;padding:1px 12px;letter-spacing:.08em}
.feat-block{position:absolute}
.feat-block h2{font-family:"Noto Serif JP",serif;font-weight:700;font-size:24px;line-height:1.5;margin:12px 0 18px;letter-spacing:.02em;white-space:nowrap}
.feat-block p{font-size:11.5px;line-height:2;color:#e4ddd6;margin-bottom:10px}
.feat-1{left:170px;top:160px;width:340px}
.feat-photo-1{left:560px;top:60px;width:580px;height:440px;background:radial-gradient(ellipse at 50% 50%,var(--bread-light) 0%,var(--bread) 40%,#5c3a1c 80%,#1a120c 100%)}
.feat-thumb-a{left:560px;top:530px;width:120px;height:80px;background:linear-gradient(135deg,#7ea25c,#d8e4c4)}
.feat-thumb-b{left:720px;top:530px;width:120px;height:80px;background:linear-gradient(135deg,#c72a22,#f1e8de)}
.feat-arrow{left:690px;top:560px}
.feat-photo-2{left:240px;top:600px;width:320px;height:280px;background:radial-gradient(ellipse at 45% 55%,#f6dc8a 0%,#d7a151 45%,#6d4520 85%)}
.feat-2{left:600px;top:680px;width:300px}
.feat-2 h2{font-size:21px}
.feat-3{left:240px;top:960px;width:300px}
.feat-3 h2{font-size:21px}
.feat-photo-3{left:560px;top:940px;width:420px;height:290px;background:linear-gradient(135deg,#b51d17 0%,#d8322a 30%,#e6b277 55%,#b51d17 100%)}
.feat-btn{left:410px;top:1300px;width:380px;height:56px}

/* products */
.products-head{left:0;top:2680px;width:1200px}
.product-lg{position:absolute;top:2750px;width:352px}
.product-lg .photo{position:relative;width:352px;height:160px}
.product-lg .label{position:absolute;left:18px;top:40px;font-family:"Noto Serif JP",serif;font-weight:700;font-size:20px;line-height:1.3;color:var(--ink)}
.product-lg .label small{display:block;font-size:10px;font-family:"Noto Sans JP",sans-serif;color:var(--muted);font-weight:500}
.product-lg p{font-size:11px;line-height:1.8;margin-top:10px;color:var(--ink)}
.product-sm{position:absolute;width:232px}
.product-sm .photo{position:relative;width:232px;height:232px}
.product-sm h3{font-size:12px;font-weight:700;margin-top:10px;line-height:1.5}
.product-sm p{font-size:10.5px;line-height:1.7;color:var(--muted)}
.products-btn{left:504px;top:3730px;width:192px;height:48px}

/* train */
.train{position:absolute;left:120px;top:3840px;width:960px;height:520px;border:1px solid var(--line)}
.train-photo{position:absolute}
.train h2{position:absolute;left:520px;top:80px;font-family:"Noto Serif JP",serif;font-weight:700;font-size:28px;line-height:1.45;letter-spacing:.03em;white-space:nowrap}
.train h2 .red{color:var(--red)}
.train .tagline{position:absolute;left:520px;top:40px;font-size:13px;font-weight:500}
.train .desc{position:absolute;left:520px;top:200px;width:380px;font-size:11px;line-height:1.9}
.price-seal{position:absolute;left:520px;top:290px;width:68px;height:68px;border-radius:50%;background:var(--red);color:var(--white);font-size:10px;display:flex;align-items:center;justify-content:center;text-align:center;line-height:1.3;font-weight:700}
.price{position:absolute;left:610px;top:292px;font-weight:700}
.price small{font-size:12px;display:block}
.price b{font-size:36px;font-family:"Noto Serif JP",serif;line-height:1.1}
.train-btn{left:610px;top:380px;width:240px;height:48px}
.train .note{position:absolute;left:520px;top:452px;font-size:10px;color:var(--muted)}

/* news */
.news-head{left:0;top:4430px;width:1200px}
.news-list{position:absolute;left:240px;top:4510px;width:720px;list-style:none}
.news-list li{display:flex;align-items:center;gap:26px;height:52px;border-bottom:1px solid var(--line);font-size:12px}
.news-list time{color:var(--muted);width:80px;font-size:11px}
.news-list .cat{border:1px solid var(--red);color:var(--red);font-size:10px;width:72px;text-align:center;line-height:1.8}
.news-more{left:860px;top:4690px;font-size:11px;color:var(--muted);letter-spacing:.12em;display:flex;align-items:center;gap:8px}

/* access */
.access-head{left:0;top:4760px;width:1200px}
.shop-info{left:240px;top:4860px;width:220px}
.shop-info .name{font-family:"Noto Serif JP",serif;font-weight:700;font-size:16px;line-height:1.2}
.shop-info .addr{font-size:10.5px;line-height:1.8;margin-top:12px}
.shop-info .hours{margin-top:10px;font-size:11px;font-weight:700;color:var(--red)}
.shop-info .tel{margin-top:6px;font-size:20px;font-weight:700;display:flex;align-items:center;gap:6px}
.shop-info .closed{font-size:10px;color:var(--muted)}
.shop-btn{left:240px;top:5050px;width:180px;height:40px;font-size:11px}
.map{left:490px;top:4850px;width:470px;height:260px;background:linear-gradient(135deg,#eef0ec 0%,#dfe6e2 50%,#cfd9e4 100%)}

/* footer */
.footer{position:absolute;left:0;top:5150px;width:1200px;height:238px;background:var(--red);color:var(--white);text-align:center}
.footer nav{display:flex;justify-content:center;gap:70px;padding-top:36px}
.footer nav a{color:var(--white);text-decoration:none;font-family:"Cormorant Garamond",serif;font-weight:600;font-size:12px;letter-spacing:.2em}
.footer .name{font-family:"Noto Serif JP",serif;font-weight:700;font-size:18px;line-height:1.2;margin-top:30px}
.footer .social-row{display:flex;justify-content:center;gap:14px;margin-top:18px}
.footer .social-row span{width:14px;height:14px;border-radius:50%;background:var(--white)}
.footer small{display:block;font-size:9px;margin-top:22px;opacity:.85;letter-spacing:.08em}
</style>
</head>
<body>

<header class="hero">
  <div class="photo hero-photo" role="img" aria-label="麦の穂と焼きたてのヤギミルククリームパンのクローズアップ写真"></div>
  <div class="hero-shade"></div>
  <nav class="global-nav">
    <div class="nav-left"><a href="#about">ABOUT</a><a href="#product">PRODUCT</a></div>
    <div class="brand-block"><span class="l1">PÂTISSERIE</span><span class="l2">SOLBE RUNELLE</span></div>
    <div class="nav-right"><a href="#news">NEWS</a><a href="#contact">CONTACT</a></div>
  </nav>
  <div class="social"><span></span><span></span><span></span></div>
  <h1 class="abs hero-title">PÂTISSERIE<br>SOLBE RUNELLE</h1>
  <p class="abs hero-lead">ヤギミルクの優しい甘さを、ひとつひとつ丁寧に。<br>海辺の小さな工房から、幸せの味をお届けします。</p>
  <div class="banner banner-bun" role="img" aria-label="ヤギミルククリームパンのバナー写真">
    <div class="txt"><small>CREAM PUFFED ROLL</small>ヤギミルク<br>クリームパン</div>
  </div>
  <div class="banner banner-rank">
    <div class="seal"></div>
    <div class="txt">通販ランキング スイーツ部門<b>最優秀賞1位</b>受賞しました</div>
  </div>
</header>

<section id="about">
  <p class="abs about-caption">美しさと可愛さの融合がコンセプトのお店です。</p>
  <div class="photo about-photo" role="img" aria-label="赤と白のストライプ屋根の店舗外観写真"></div>
  <div class="abs about-text">
    <p class="eyebrow">ABOUT</p>
    <h2 class="section-title">当店について</h2>
    <p>ソルベリュンヌは、ヤギのミルクを使ったお菓子を作るパティスリーです。</p>
    <p>牧場で育ったヤギたちの新鮮なミルクを毎朝受け取り、一つひとつ手作業で仕上げています。</p>
    <p>店のシンボルはヤギのクラリス。アートとかわいらしさが同居する空間で、特別なひとときをお過ごしください。</p>
    <a class="btn btn-black about-btn">詳しく見る</a>
  </div>
</section>

<section class="feature">
  <div class="photo feat-photo-1" role="img" aria-label="麦の穂と並ぶクリームパンの写真"></div>
  <div class="feat-block feat-1">
    <span class="tag-red">人気No.1商品</span>
    <h2>ヤギミルクのクリームパン</h2>
    <p>ふわふわの生地の中に、ヤギミルクをたっぷり使った特製クリームを詰め込みました。</p>
    <p>やさしい甘さとコクのある味わいは、お子様から大人まで幅広く愛されています。</p>
    <p>冷凍でお届けするので、いつでも焼きたての美味しさをお楽しみいただけます。</p>
  </div>
  <div class="photo feat-thumb-a" role="img" aria-label="牧場のヤギの写真"></div>
  <svg class="abs feat-arrow" width="20" height="20" viewBox="0 0 20 20"><path d="M4 4l12 12M16 4L4 16" stroke="#fff" stroke-width="1.5"/></svg>
  <div class="photo feat-thumb-b" role="img" aria-label="店舗の写真"></div>

  <div class="photo feat-photo-2" role="img" aria-label="断面から黄色いクリームが見えるパンの写真"></div>
  <div class="feat-block feat-2">
    <h2>ヤギミルクの<br>香りが際立つ。</h2>
    <p>クリームには牧場直送のヤギミルクを使用。ほのかな香りとまろやかな口どけが特徴です。</p>
    <p>素材本来の味を活かすため、甘さは控えめに仕上げました。</p>
  </div>

  <div class="feat-block feat-3">
    <h2>焼きたての味わい<br>そのままの急速冷凍。</h2>
    <p>焼き上げた直後に急速冷凍することで、香りと食感を閉じ込めています。</p>
    <p>解凍してトースターで温めるだけで、お店の味がご自宅で楽しめます。</p>
  </div>
  <div class="photo feat-photo-3" role="img" aria-label="赤い箱に詰められたクリームパンの写真"></div>
  <a class="btn btn-red feat-btn">他の商品を購入する</a>
</section>

<section id="product">
  <div class="abs products-head"><p class="eyebrow">PRODUCT</p><h2 class="section-title">その他の商品</h2></div>

  <article class="product-lg" style="left:240px">
    <div class="photo" role="img" aria-label="ヤギミルクプリンの瓶の写真" style="background:linear-gradient(90deg,#f3ebdc,#e8dcc4 60%,#cfc2a6)">
      <span class="label"><small>濃厚なのに優しい</small>ヤギミルク<br>プリン</span>
    </div>
    <p>牧場のヤギミルクをたっぷり使った、なめらかな口当たりの自家製プリンです。</p>
  </article>
  <article class="product-lg" style="left:608px">
    <div class="photo" role="img" aria-label="ヤギミルクの瓶の写真" style="background:linear-gradient(90deg,#f3ebdc,#e3e6d4 60%,#bfcaa8)">
      <span class="label"><small>牧場から直送</small>グラスフェッド<br>ヤギミルク</span>
    </div>
    <p>草を食べて育ったヤギから搾った、新鮮でさっぱりとしたミルクです。</p>
  </article>

  <article class="product-sm" style="left:240px;top:3020px">
    <div class="photo" role="img" aria-label="赤い箱とチーズケーキの写真" style="background:linear-gradient(135deg,#c42a22,#e9b26a)"></div>
    <h3>ヤギミルクチーズケーキ</h3><p>濃厚でありながら後味すっきりの人気商品です。</p>
  </article>
  <article class="product-sm" style="left:484px;top:3020px">
    <div class="photo" role="img" aria-label="層になったケーキの写真" style="background:linear-gradient(135deg,#e8d3b4,#a5704a)"></div>
    <h3>ミルクレープ</h3><p>薄い生地とクリームを何層にも重ねました。</p>
  </article>
  <article class="product-sm" style="left:728px;top:3020px">
    <div class="photo" role="img" aria-label="モンブランの写真" style="background:linear-gradient(135deg,#6b4a33,#d9a66b)"></div>
    <h3>マロンモンブラン</h3><p>栗の風味とミルククリームの相性が抜群です。</p>
  </article>
  <article class="product-sm" style="left:240px;top:3370px">
    <div class="photo" role="img" aria-label="缶に入った焼き菓子の写真" style="background:linear-gradient(135deg,#e3e3e0,#9fb1c2)"></div>
    <h3>ヤギミルククッキー</h3><p>サクッと軽い食感の焼き菓子詰め合わせ。</p>
  </article>
  <article class="product-sm" style="left:484px;top:3370px">
    <div class="photo" role="img" aria-label="瓶入りミルクジャムの写真" style="background:linear-gradient(135deg,#f4efe6,#d7c29a)"></div>
    <h3>ミルクジャム</h3><p>パンやヨーグルトに合うやさしい甘さ。</p>
  </article>
  <article class="product-sm" style="left:728px;top:3370px">
    <div class="photo" role="img" aria-label="焼きたてのパンケーキの写真" style="background:linear-gradient(135deg,#8a5a2c,#e7b46b)"></div>
    <h3>ミルクパンケーキ</h3><p>ふんわり厚焼きの週末限定メニューです。</p>
  </article>
  <a class="btn btn-black products-btn">すべての商品を見る</a>
</section>

<section class="train">
  <div class="train-photo" role="img" aria-label="赤い列車の写真" style="left:30px;top:40px;width:200px;height:190px;background:linear-gradient(135deg,#b9231c,#e8e1d6)"></div>
  <div class="train-photo" role="img" aria-label="列車内でスイーツを楽しむ様子の写真" style="left:240px;top:40px;width:240px;height:190px;background:linear-gradient(135deg,#6e2a22,#cf4b3d)"></div>
  <div class="train-photo" role="img" aria-label="スイーツのプレートの写真" style="left:30px;top:240px;width:200px;height:220px;background:linear-gradient(135deg,#f1e3d0,#c9945e)"></div>
  <div class="train-photo" role="img" aria-label="牧場の風景写真" style="left:240px;top:240px;width:240px;height:220px;background:linear-gradient(135deg,#9bb37a,#e6e2d3)"></div>
  <p class="tagline">まちかどテレビで特集！全国から集客した</p>
  <h2>潮風鉄道ソルベリュンヌの<br><span class="red">スイーツ列車。</span></h2>
  <p class="desc">海沿いを走る列車の中で、ソルベリュンヌのスイーツを味わう特別な旅。車窓の景色とともに、ここでしか食べられない限定メニューをお楽しみください。</p>
  <div class="price-seal">乗車料金<br>込み</div>
  <p class="price"><small>お一人様</small><b>4,500</b>円(税別)</p>
  <a class="btn btn-red train-btn">今すぐ申し込む</a>
  <p class="note">※運行日は季節により異なります。詳しくはお問い合わせください。</p>
</section>

<section id="news">
  <div class="abs news-head"><p class="eyebrow">NEWS</p><h2 class="section-title">最新情報</h2></div>
  <ul class="news-list">
    <li><time>2019.08.01</time><span class="cat">お知らせ</span><span>ホームページをリニューアルしました</span></li>
    <li><time>2019.07.20</time><span class="cat">メディア</span><span>テレビ番組で当店のスイーツ列車が紹介されました</span></li>
    <li><time>2019.07.05</time><span class="cat">新商品</span><span>夏限定のヤギミルクジェラートを発売しました</span></li>
  </ul>
  <p class="abs news-more">READ MORE
    <svg width="22" height="8" viewBox="0 0 22 8"><path d="M0 4h20M16 1l4 3-4 3" fill="none" stroke="#7a716b"/></svg>
  </p>
</section>

<section id="contact">
  <div class="abs access-head"><p class="eyebrow">ACCESS</p><h2 class="section-title">アクセス</h2></div>
  <div class="abs shop-info">
    <p class="name">PÂTISSERIE<br>SOLBE RUNELLE</p>
    <p class="addr">〒000-0000<br>海辺町1-2-3 みなと通り</p>
    <p class="hours">OPEN 10:00 − CLOSE 19:00</p>
    <p class="tel">
      <svg width="16" height="16" viewBox="0 0 24 24"><path d="M6.6 10.8a15 15 0 0 0 6.6 6.6l2.2-2.2a1 1 0 0 1 1-.25 11.4 11.4 0 0 0 3.6.57 1 1 0 0 1 1 1V20a1 1 0 0 1-1 1A17 17 0 0 1 3 4a1 1 0 0 1 1-1h3.5a1 1 0 0 1 1 1c0 1.25.2 2.45.57 3.57a1 1 0 0 1-.25 1z" fill="#2b2623"/></svg>
      0193-00-4821
    </p>
    <p class="closed">定休日：水曜日</p>
  </div>
  <a class="btn btn-black shop-btn">メールでお問い合わせ</a>
  <div class="photo map" role="img" aria-label="店舗周辺の地図"></div>
</section>

<footer class="footer">
  <nav><a href="#about">ABOUT</a><a href="#product">PRODUCT</a><a href="#news">NEWS</a><a href="#contact">CONTACT</a></nav>
  <p class="name">PÂTISSERIE<br>SOLBE RUNELLE</p>
  <div class="social-row"><span></span><span></span><span></span></div>
  <small>Copyright © SOLBE RUNELLE All Rights Reserved.</small>
</footer>

</body>
</html>
```